Harriet Voss Consortium - Paediatric Lower Limb Surgery Agenda Forming Collective

A 2-sided A4 leaflet to explain the research priorities in Children's Orthopaedic Surgery.
We would like this to be similar to that produced previously by the physiotherapists.

```html
<!DOCTYPE html>
<html lang="en">
<head>
<meta charset="utf-8">
<title>Harriet Voss Consortium – Leaflet</title>
<link href="https://fonts.googleapis.com/css2?family=Oswald:wght@400;500;600&family=Lato:ital,wght@0,400;0,700;0,900;1,400;1,700&display=swap" rel="stylesheet">
<style>
  :root{
    --stage-bg:#6b6b6b;
    --paper:#ffffff;
    --ink:#333333;
    --grey:#4a4a4a;
    --red:#e31e2d;
    --orange:#f5a300;
    --orange-deep:#e8801d;
    --lime:#d3d12a;
    --mint:#9fcbbd;
    --teal:#0d8e98;
    --blue:#3c4aa6;
    --blue-soft:#3f4fa3;
    --green:#3f9a7c;
    --green-soft:#a9d3c4;
    --society:#2a3c8f;
    --consortium:#8a1c2a;
  }
  *{box-sizing:border-box;margin:0;padding:0}
  html,body{width:1200px;height:902px;overflow:hidden}
  body{background:var(--stage-bg);font-family:"Lato",sans-serif;color:var(--ink);position:relative}
  .page{position:absolute;background:var(--paper);box-shadow:0 4px 14px rgba(0,0,0,.35);overflow:hidden}
  .page--front{left:53px;top:55px;width:510px;height:714px}
  .page--back{left:628px;top:134px;width:510px;height:715px}
  .deco{position:absolute;left:0;top:0}

  /* front */
  .org-mark{position:absolute;display:flex;align-items:center;gap:7px;font-weight:700}
  .org-mark__dot{width:13px;height:13px;border-radius:50%;background:currentColor;flex:none}
  .org-mark--society{left:48px;top:122px;font-size:11px;color:var(--society)}
  .org-mark--consortium{left:318px;top:34px;font-size:17px;line-height:1.05;color:var(--consortium);width:150px}
  .headline{position:absolute;left:250px;top:98px;font-family:"Oswald",sans-serif;white-space:nowrap}
  .headline__name{display:block;color:var(--red);font-size:22px;font-weight:500;line-height:1.2}
  .headline__line{display:block;color:#222;font-size:19px;font-weight:400;line-height:28px}
  .headline__line:nth-child(2){padding-left:8px}
  .headline__line:nth-child(3){padding-left:22px}
  .headline__line:nth-child(4){padding-left:48px}
  .photo{position:absolute;left:0;top:170px;width:205px;height:300px;background:linear-gradient(160deg,#f3f5f6 0%,#e2e6e8 45%,#b9bdc0 100%)}
  .intro{position:absolute;left:213px;top:266px;width:272px;font-size:11.4px;line-height:1.32;text-align:justify;hyphens:auto}
  .intro p+p{margin-top:10px}
  .band{position:absolute;left:0;top:523px;width:510px;height:146px;background:var(--orange-deep)}
  .stage{position:absolute;top:441px;width:152px;height:226px;border-radius:14px 14px 0 0;overflow:hidden;color:#fff}
  .stage__head{height:82px;text-align:center;padding-top:11px}
  .stage__label{font-family:"Lato",sans-serif;font-size:15px;font-weight:900;letter-spacing:.5px}
  .stage__word{font-weight:900;font-size:32px;line-height:1.1;letter-spacing:-.5px}
  .stage__body{height:144px;padding:8px 10px;font-size:10px;font-weight:700;line-height:1.22;text-align:justify;hyphens:auto}
  .stage--ask{left:19px}
  .stage--ask .stage__head{background:var(--blue)}
  .stage--ask .stage__body{background:var(--blue-soft)}
  .stage--analyse{left:180px}
  .stage--analyse .stage__head{background:linear-gradient(180deg,#e8302c,#f28a1e)}
  .stage--analyse .stage__body{background:var(--orange)}
  .stage--analyse .stage__word{font-size:25px;padding-top:5px}
  .stage--prioritise{left:341px}
  .stage--prioritise .stage__head{background:var(--green)}
  .stage--prioritise .stage__body{background:var(--green-soft);color:#2b2b2b}
  .stage--prioritise .stage__word{font-size:20px;padding-top:9px}
  .partners{position:absolute;left:0;top:678px;width:510px;display:flex;justify-content:center;gap:34px;align-items:center}
  .partner{display:flex;align-items:center;gap:7px;font-size:11.5px;font-weight:700;color:#333}
  .partner__shape{width:13px;height:13px;background:var(--red);flex:none}
  .partner__shape--round{border-radius:50%;background:#333}

  /* back */
  .back-title{position:absolute;left:0;top:20px;width:510px;text-align:center;font-family:"Oswald",sans-serif;font-weight:500;font-size:31px;color:#fff;letter-spacing:.3px}
  .back-title__accent{color:var(--orange)}
  .priorities{position:absolute;left:0;top:0;list-style:none}
  .priority{position:absolute;left:0;width:510px;height:48px}
  .priority__num{position:absolute;left:30px;top:0;width:40px;height:44px;font-family:"Oswald",sans-serif;font-weight:600;font-size:28px;color:#fff;text-align:center;line-height:44px}
  .priority__bar{position:absolute;left:118px;top:1px;width:381px;height:34px;border-radius:7px;padding:0 10px;display:flex;align-items:center;font-size:8.8px;line-height:1.2;color:#2b2b2b;box-shadow:0 2px 3px rgba(0,0,0,.2)}
  .priority--orange .priority__bar{background:var(--orange)}
  .priority--lime .priority__bar{background:var(--lime)}
  .priority--mint .priority__bar{background:var(--mint)}
  .priority--teal .priority__bar{background:var(--teal);color:#fff}
  .thanks{position:absolute;left:0;top:640px;width:510px;text-align:center;font-style:italic}
  .thanks__lead{font-size:9.4px;font-weight:700;line-height:1.25;color:#222}
  .thanks__head{font-size:11px;font-weight:700;color:var(--red);margin:4px 0 2px}
  .thanks__list{font-size:6.4px;line-height:1.3;color:#222}
</style>
</head>
<body>

<section class="page page--front" aria-label="Leaflet front">
  <svg class="deco" width="510" height="714" viewBox="0 0 510 714" aria-hidden="true">
    <path d="M0 150 C60 140 150 138 235 150 L235 160 C150 150 70 156 0 168 Z" fill="var(--grey)"/>
    <path d="M0 168 C70 150 150 148 235 158 L235 168 C150 162 70 168 0 186 Z" fill="var(--red)"/>
    <path d="M268.5 0 A160 160 0 0 0 243.7 150" fill="none" stroke="var(--grey)" stroke-width="11"/>
    <path d="M243.7 150 A160 160 0 0 0 510 209.5" fill="none" stroke="var(--orange-deep)" stroke-width="11"/>
  </svg>

  <div class="org-mark org-mark--society"><span class="org-mark__dot"></span>Northfield Orthopaedic Society</div>
  <div class="org-mark org-mark--consortium"><span class="org-mark__dot"></span>Harriet Voss Consortium</div>

  <h1 class="headline">
    <span class="headline__name">HARRIET VOSS CONSORTIUM -</span>
    <span class="headline__line">Paediatric Lower Limb</span>
    <span class="headline__line">Surgery Agenda Forming</span>
    <span class="headline__line">Collective</span>
  </h1>

  <div class="photo" role="img" aria-label="Photo of a physiotherapist helping a young boy walk in a bright clinic"></div>

  <div class="intro">
    <p>Surgery is often carried out amongst children with conditions that their legs, but in many conditions, it is not known which treatment works best. We need high-quality research to test which treatments are better for children.</p>
    <p>We reached out to everybody involved with children who have orthopaedic problems affecting their legs (from hip to toes), including children, parents, carers, charity workers, and all the professional groups. We asked all for their views on identifying the most important unanswered questions.</p>
  </div>

  <div class="band"></div>

  <article class="stage stage--ask">
    <div class="stage__head"><div class="stage__label">STAGE 1</div><div class="stage__word">ASK</div></div>
    <div class="stage__body">Our UK-wide survey of patients, carers, physiotherapists, nurses and surgeons asked “What is the most important unanswered question amongst children undergoing planned surgery for conditions affecting their legs”</div>
  </article>
  <article class="stage stage--analyse">
    <div class="stage__head"><div class="stage__label">STAGE 2</div><div class="stage__word">ANALYSE</div></div>
    <div class="stage__body">We reviewed 1023 questions from 388 people, and sorted these into 76 unique themed questions.</div>
  </article>
  <article class="stage stage--prioritise">
    <div class="stage__head"><div class="stage__label">STAGE 1</div><div class="stage__word">PRIORITISE</div></div>
    <div class="stage__body">From those we asked patients, carers, physiotherapists, nurses and surgeons to tell us “What are your top-10 most important questions”. This created a shortlist that were prioritized at a final workshop.</div>
  </article>

  <div class="partners">
    <div class="partner"><span class="partner__shape partner__shape--round"></span>Avonmere University</div>
    <div class="partner"><span class="partner__shape"></span>SYLS Society for Young Limb Surgery</div>
  </div>
</section>

<section class="page page--back" aria-label="Leaflet back">
  <svg class="deco" width="510" height="715" viewBox="0 0 510 715" aria-hidden="true">
    <defs>
      <linearGradient id="headBand" x1="0" y1="0" x2="0" y2="1">
        <stop offset="0" stop-color="#3a3a3a"/><stop offset="1" stop-color="#5a5a5a"/>
      </linearGradient>
      <g id="ribbon">
        <path d="M30 0 H70 V34 L50 46 L30 34 Z"/>
        <path d="M70 2 H118 V32 H70 Z" opacity=".8"/>
      </g>
    </defs>
    <path d="M0 0 H510 V88 C360 72 160 74 0 96 Z" fill="url(#headBand)"/>
    <path d="M0 96 C160 74 360 72 510 88 L510 102 C360 84 160 88 0 108 Z" fill="var(--red)"/>
    <path d="M0 640 C150 612 360 610 510 632 L510 620 C360 598 150 600 0 628 Z" fill="var(--red)"/>
    <use href="#ribbon" y="111" fill="var(--orange)"/>
    <use href="#ribbon" y="163" fill="var(--lime)"/>
    <use href="#ribbon" y="215" fill="var(--mint)"/>
    <use href="#ribbon" y="267" fill="var(--teal)"/>
    <use href="#ribbon" y="319" fill="var(--lime)"/>
    <use href="#ribbon" y="371" fill="var(--orange)"/>
    <use href="#ribbon" y="423" fill="var(--teal)"/>
    <use href="#ribbon" y="475" fill="var(--mint)"/>
    <use href="#ribbon" y="527" fill="var(--lime)"/>
    <use href="#ribbon" y="579" fill="var(--orange)"/>
  </svg>

  <h2 class="back-title"><span class="back-title__accent">OUR TOP-10</span> RESEARCH PRIORITIES:</h2>

  <ol class="priorities">
    <li class="priority priority--orange" style="top:111px"><span class="priority__num">1</span><p class="priority__bar">What are the best ways to measure the outcome following lower limb orthopaedic surgery in children?</p></li>
    <li class="priority priority--lime" style="top:163px"><span class="priority__num">2</span><p class="priority__bar">Following orthopaedic surgery to the lower limbs, what should children’s rehabilitation include, how long is it expected to last and how does it affect the result of treatment?</p></li>
    <li class="priority priority--mint" style="top:215px"><span class="priority__num">3</span><p class="priority__bar">What is the short-term and long-term clinical and cost effectiveness of orthopaedic lower limb surgery (including best timing and technique) for children with Cerebral Palsy who can walk?</p></li>
    <li class="priority priority--teal" style="top:267px"><span class="priority__num">4</span><p class="priority__bar">What are the short term and long term outcomes of surgery compared to non-surgical care in the treatment of Perthes disease of the hip?</p></li>
    <li class="priority priority--lime" style="top:319px"><span class="priority__num">5</span><p class="priority__bar">What is the clinical and cost effectiveness of pre-operative rehabilitation in children presenting with lower limb orthopaedic conditions?</p></li>
    <li class="priority priority--orange" style="top:371px"><span class="priority__num">6</span><p class="priority__bar">What is the short-term and long-term clinical and cost effectiveness of Selective Dorsal Rhizotomy (SDR) in children with Cerebral Palsy who can walk?</p></li>
    <li class="priority priority--teal" style="top:423px"><span class="priority__num">7</span><p class="priority__bar">Can surveillance and non-surgical treatment (e.g. physiotherapy, botulinum toxin injections, functional electrical stimulation, orthotics, casting) prevent the development of deformity requiring surgery in children with Cerebral Palsy?</p></li>
    <li class="priority priority--mint" style="top:475px"><span class="priority__num">8</span><p class="priority__bar">What is the best method of screening for Developmental Dysplasia of the Hip (DDH) in terms of clinical and cost effectiveness?</p></li>
    <li class="priority priority--lime" style="top:527px"><span class="priority__num">9</span><p class="priority__bar">What are the best strategies to optimise communication of information between patients/carers and clinicians in order to enable shared decision-making?</p></li>
    <li class="priority priority--orange" style="top:579px"><span class="priority__num">10</span><p class="priority__bar">What is the best management for hip displacement in children with Cerebral Palsy?</p></li>
  </ol>

  <div class="thanks">
    <p class="thanks__lead">Many thanks to all those people who helped us<br>take this work off the ground and helped us finish it!</p>
    <p class="thanks__head">Special thanks to:</p>
    <p class="thanks__list">The Society for Young Limb Surgery<br>The Northfield Orthopaedic Society<br>The Avonmere University and the<br>Harriet Voss Consortium, who always look for fair play in research!</p>
  </div>
</section>

</body>
</html>
```